Heritage Depot Business Cards

Require a business card design. <br/><br/>Needs to include logo (either round or long version) plus these details:<br/>Maya Corvell<br/>Heritage Depot<br/>maya@brightmarttrade.com.au<br/>02 6418 7395<br/>PO Box Glenfarrow NSW 2791<br/>www.heritagedepot.com.au<br/><br/>I need in an editable format so that I can create for multiple staff members. <br/><br/>

Target Market(s)

We are an online store selling renovation products to home owners are builders. Looking for a classic classy design.

Industry/Entity Type

Home And Garden

Contact Information for Business Card

Maya Corvell
Heritage Depot
maya@brightmarttrade.com.au
02 6418 7395
PO Box Glenfarrow NSW 2791
www.heritagedepot.com.au

Colors

Designer to choose colors to be used in the design.

Requirements
Must have
• Must include Logo.

```html
<!DOCTYPE html>
<html lang="en">
<head>
<meta charset="utf-8">
<title>Heritage Depot Business Cards</title>
<link rel="stylesheet" href="https://fonts.googleapis.com/css2?family=Roboto+Slab:wght@700&family=Work+Sans:wght@400;500&display=swap">
<style>
  :root {
    --bg: #141414;
    --card: #222222;
    --card-edge: #2c2c2c;
    --ink: #f2f2f2;
    --ink-soft: #d6d6d6;
    --front-mark: #8a8a8a;
    --rule: #e6e6e6;
  }
  * { margin: 0; padding: 0; box-sizing: border-box; }
  html, body { width: 1200px; height: 900px; overflow: hidden; }
  body {
    background: var(--bg);
    font-family: "Work Sans", sans-serif;
    color: var(--ink);
    display: flex;
    flex-direction: column;
    align-items: center;
    justify-content: center;
    gap: 34px;
  }
  .card {
    width: 700px;
    height: 400px;
    background: linear-gradient(135deg, var(--card-edge), var(--card));
    box-shadow: 0 14px 40px rgba(0,0,0,0.55);
    position: relative;
  }
  .card-front {
    display: flex;
    align-items: center;
    justify-content: center;
  }
  .front-wordmark {
    font-family: "Work Sans", sans-serif;
    font-weight: 500;
    font-size: 54px;
    color: var(--front-mark);
    letter-spacing: 0.5px;
  }
  .card-back {
    display: flex;
    align-items: center;
    padding: 0 50px 0 56px;
  }
  .brand-badge {
    width: 210px;
    height: 210px;
    border: 1.5px solid var(--rule);
    border-radius: 50%;
    display: flex;
    align-items: center;
    justify-content: center;
    flex-shrink: 0;
  }
  .brand-name {
    font-family: "Work Sans", sans-serif;
    font-weight: 500;
    font-size: 30px;
    line-height: 1.05;
    text-align: center;
    color: var(--ink);
  }
  .divider {
    width: 1.5px;
    height: 190px;
    background: var(--rule);
    margin: 0 44px 0 40px;
    flex-shrink: 0;
  }
  .contact { display: flex; flex-direction: column; }
  .person-name {
    font-family: "Roboto Slab", serif;
    font-weight: 700;
    font-size: 33px;
    letter-spacing: 3px;
    text-transform: uppercase;
    line-height: 1;
  }
  .company {
    font-size: 19px;
    color: var(--ink-soft);
    margin-top: 6px;
    margin-bottom: 12px;
  }
  .address {
    font-size: 19px;
    line-height: 1.3;
    color: var(--ink-soft);
    margin-bottom: 10px;
  }
  .contact-line {
    display: flex;
    align-items: center;
    gap: 9px;
    font-size: 19px;
    line-height: 1.4;
    color: var(--ink-soft);
  }
  .contact-line svg { width: 13px; height: 13px; flex-shrink: 0; }
</style>
</head>
<body>
  <section class="card card-front">
    <div class="front-wordmark">Heritage Depot</div>
  </section>

  <section class="card card-back">
    <div class="brand-badge">
      <div class="brand-name">Heritage<br>Depot</div>
    </div>
    <div class="divider"></div>
    <div class="contact">
      <div class="person-name">Maya Corvell</div>
      <div class="company">Heritage Depot</div>
      <div class="address">PO Box Glenfarrow<br>NSW 2791</div>
      <div class="contact-line">
        <svg viewBox="0 0 16 16" fill="none" stroke="currentColor" stroke-width="1.6" aria-hidden="true"><path d="M4 1.5l2.5 3-1.5 1.5a8 8 0 0 0 5 5l1.5-1.5 3 2.5-1.5 2.5C7 14 2 9 1.5 3z"/></svg>
        <span>02 6418 7395</span>
      </div>
      <div class="contact-line">
        <svg viewBox="0 0 16 16" fill="none" stroke="currentColor" stroke-width="1.6" aria-hidden="true"><rect x="1.5" y="3.5" width="13" height="9"/><path d="M1.5 3.5l6.5 5 6.5-5"/></svg>
        <span>maya@brightmarttrade.com.au</span>
      </div>
      <div class="contact-line">
        <svg viewBox="0 0 16 16" fill="none" stroke="currentColor" stroke-width="1.4" aria-hidden="true"><circle cx="8" cy="8" r="6.5"/><ellipse cx="8" cy="8" rx="3" ry="6.5"/><path d="M1.5 8h13"/></svg>
        <span>www.heritagedepot.com.au</span>
      </div>
    </div>
  </section>
</body>
</html>
```